New Web Design Project- Maplebrook Elders

Maplebrook Elders is the Capital regions premiere, non-medical, in-home care & companionship service that unites "junior-senior" caregivers with "senior-senior" care recipients so that senior-seniors can remain safe & independent in their own homes.
Our compassionate "junior-senior" caregivers are all retirees that have already enjoyed rewarding careers and/or have raised families of their own and feel the need to pay-it-forward with their care for older seniors.
Services include grocery shopping, medical or dental appointments, errands, meal preparation & cleanup, light housekeeping, bed making, laundry, hobbies, reading, transportation, entertainment, games, mobility assistance/transfers, respite care, light yard work, pet walking.

Target Market(s)

Grown children of senior-seniors between who are between 55-70, predominantly the daughters (female). End users of services (senior-seniors) are typically 80-100 years old and living in own homes

Font styles to use
Sans Serif

Colors
3277b5
ec1f27

Requirements
Must have
• supporting photos on each page. Contact us page. Promotional video (done) attached that doesn't take viewers off my site (https://vidsharehub.example/watch/Qm7rTz2KpLw).
• Also, need my downloadable brochure (attached).
• The following pages:
• Home. Services. About Us. News. Employment. Contact us. Junior-Seniors Assisting Senior-Seniors. Why non-medical in-home care. Who are junior-seniors?Financial effects of senior care. Do you need care? Does someone you love need care?
Should not have
• Any other photos or images other than what I've supplied.

```html
<!DOCTYPE html>
<html lang="en">
<head>
<meta charset="utf-8">
<title>Maplebrook Elders – Home</title>
<link rel="stylesheet" href="https://fonts.googleapis.com/css2?family=Libre+Baskerville:wght@700&family=Montserrat:wght@400;500;600;700&display=swap">
<style>
:root{
  --navy:#1b3f7e;
  --red:#c21b2f;
  --red-line:rgba(255,255,255,.45);
  --ink:#3b3b3b;
  --muted:#5a5a5a;
  --white:#ffffff;
  --paper:#f4f2ef;
}
*{box-sizing:border-box;margin:0;padding:0}
html,body{width:1200px;height:4027px;overflow:hidden}
body{font-family:"Montserrat",sans-serif;color:var(--ink);background:var(--white);position:relative}
.serif{font-family:"Libre Baskerville",serif}
.abs{position:absolute}

/* header */
.site-header{position:absolute;left:0;top:0;width:1200px;height:113px;background:var(--white)}
.brand{position:absolute;left:54px;top:34px;display:flex;align-items:center;gap:12px}
.brand-square{width:34px;height:34px;background:var(--navy)}
.brand-name{font-family:"Montserrat",sans-serif;font-weight:600;font-size:22px;color:var(--navy)}
.main-nav a{position:absolute;top:44px;font-size:15px;font-weight:500;color:var(--navy);text-decoration:none}

/* buttons */
.btn-outline{position:absolute;display:flex;align-items:center;justify-content:center;border:2px solid var(--navy);color:var(--navy);font-size:17px;font-weight:500;background:transparent}
.btn-outline.red{border-color:var(--red);color:var(--red)}

/* hero */
.hero{position:absolute;left:0;top:113px;width:1200px;height:714px;background:linear-gradient(90deg,#d9cfc6 0%,#e8e2dc 35%,#dfe6ee 60%,#eef2f6 100%)}
.hero-title{position:absolute;left:628px;top:272px;font-size:44px;line-height:1.12;color:var(--navy)}
.hero-btn{position:absolute;left:628px;top:389px;width:232px;height:46px;background:var(--navy);color:var(--white);font-family:"Libre Baskerville",serif;font-size:18px;display:flex;align-items:center;justify-content:center}

/* section headings */
.heading{font-family:"Libre Baskerville",serif;font-weight:700;font-size:32px;line-height:1.35}
.heading.navy{color:var(--navy)}
.heading.red{color:var(--red)}
.rule{height:4px;width:110px;position:absolute}
.body-copy{font-size:15.5px;line-height:2;color:var(--muted)}

/* who */
.who-photo{left:54px;top:910px;width:526px;height:352px;background:linear-gradient(135deg,#8a5a3f,#c9a88c 55%,#6e7a5a)}

/* services */
.services{position:absolute;left:0;top:1334px;width:1200px;height:618px;background:var(--red)}
.services-title{position:absolute;left:54px;top:158px;color:var(--white);font-size:32px}
.services-rule{left:54px;top:213px;background:var(--white);width:106px;height:3px}
.services-copy{position:absolute;left:54px;top:240px;width:528px;color:var(--white);font-size:15px;line-height:2;text-align:justify}
.service-grid{position:absolute;left:596px;top:76px;width:551px;height:470px;display:grid;grid-template-columns:1fr 1fr 1fr;grid-template-rows:1fr 1fr 1fr}
.service{display:flex;flex-direction:column;align-items:center;justify-content:center;color:var(--white);font-size:16px;font-weight:500;text-align:center;line-height:1.6;border-color:var(--red-line);border-style:solid;border-width:0}
.service svg{width:52px;height:52px;margin-bottom:8px;fill:none;stroke:var(--white);stroke-width:2.4;stroke-linecap:round;stroke-linejoin:round}
.service.c2,.service.c3{border-left-width:1px}
.service.r2,.service.r3{border-top-width:1px}
.service.more{font-family:"Libre Baskerville",serif;font-size:20px}

/* why */
.why-list{position:absolute;left:54px;top:2170px;list-style:none;font-size:15.5px;color:var(--muted);line-height:1.6}
.why-list li{position:relative;padding-left:44px;margin-bottom:12px;width:540px}
.why-list li::before{content:"";position:absolute;left:0;top:6px;width:12px;height:12px;background:var(--red)}
.why-photo{left:612px;top:2027px;width:535px;height:355px;background:linear-gradient(135deg,#7b8c4a,#cfc4b2 50%,#6b5a44)}

/* financial */
.finance{position:absolute;left:0;top:2449px;width:1200px;height:727px;background:linear-gradient(90deg,#f6f3ef 0%,#efe9e3 50%,#e6e0da 100%)}
.finance-photo{position:absolute;left:640px;top:0;width:560px;height:727px;background:linear-gradient(180deg,#e9e3dc,#d8c8bb 50%,#efeae4)}
.cost-table{position:absolute;left:54px;top:2803px;border-collapse:collapse;font-size:14.5px;color:var(--ink)}
.cost-table th{font-family:"Libre Baskerville",serif;font-size:18px;color:var(--navy);text-align:left;padding-bottom:8px}
.cost-table td{padding:3px 0;line-height:1.6}
.col1{width:202px}.col2{width:222px}

/* cards */
.card{position:absolute;top:3262px;width:333px;height:290px;display:flex;align-items:center;justify-content:center;text-align:center}
.card-photo{position:absolute;inset:0;background:linear-gradient(135deg,#3a3430,#6a5a4c 55%,#2e2a27)}
.card-title{position:relative;color:var(--white);font-family:"Libre Baskerville",serif;font-size:20px;line-height:1.5;padding:0 30px}

/* footer */
.site-footer{position:absolute;left:0;top:3635px;width:1200px;height:325px;background:var(--navy);color:var(--white)}
.footer-brand{position:absolute;left:54px;top:120px;display:flex;align-items:center;gap:12px}
.footer-brand .brand-square{background:var(--white)}
.footer-brand .brand-name{color:var(--white);font-size:24px}
.footer-heading{position:absolute;top:60px;font-size:19px;font-weight:600;letter-spacing:.5px}
.contact-list{position:absolute;left:422px;top:110px;font-size:14.5px;line-height:2.4;list-style:none}
.socials{position:absolute;left:422px;top:276px;display:flex;gap:13px}
.socials span{width:26px;height:26px;border-radius:50%;background:var(--white)}
.newsletter-text{position:absolute;left:800px;top:108px;width:360px;font-size:14.5px;line-height:1.55}
.newsletter-form{position:absolute;left:800px;top:175px;display:flex;height:42px}
.newsletter-form .field{width:240px;border:2px solid var(--white);display:flex;align-items:center;padding-left:18px;font-size:15px}
.newsletter-form .submit{width:110px;background:var(--white);color:var(--navy);font-weight:700;font-size:15px;display:flex;align-items:center;justify-content:center}
.legal{position:absolute;left:0;top:3960px;width:1200px;height:67px;display:flex;align-items:center;justify-content:center;font-size:15px;font-weight:700;color:var(--navy);letter-spacing:.5px}
</style>
</head>
<body>

<header class="site-header">
  <div class="brand"><span class="brand-square"></span><span class="brand-name">Maplebrook Elders</span></div>
  <nav class="main-nav">
    <a style="left:466px">Home</a>
    <a style="left:578px">Services</a>
    <a style="left:690px">About Us</a>
    <a style="left:802px">News</a>
    <a style="left:914px">Employment</a>
    <a style="left:1064px">Contact us</a>
  </nav>
</header>

<section class="hero" role="img" aria-label="Photo of a smiling older woman with white curly hair">
  <h1 class="hero-title serif">The care and company<br>you need to be at home</h1>
  <a class="hero-btn">Watch video</a>
</section>

<section class="who">
  <div class="abs who-photo" role="img" aria-label="Photo of a caregiver and an older woman preparing a salad in a kitchen"></div>
  <h2 class="abs heading navy" style="left:612px;top:915px;width:540px">Who are “Junior Seniors” at Maplebrook Elders™?</h2>
  <p class="abs body-copy" style="left:612px;top:1030px;width:540px">With most non-medical, in-home care and companionship services, there can be a vast disconnect between the age, interests and socio-economic backgrounds of the caregivers and their respective senior clients.</p>
  <a class="btn-outline" style="left:612px;top:1173px;width:188px;height:48px">Read More</a>
</section>

<section class="services">
  <h2 class="services-title serif">Our Services</h2>
  <div class="rule services-rule"></div>
  <p class="services-copy">Lorem ipsum dolor sit amet, consectetur adipiscing elit, sed do eiusmod tempor incididunt ut labore et dolore magna aliqua. Ut enim ad minim veniam, quis nostrud exercitation ullamco laboris nisi ut aliquip ex ea commodo consequat. Duis aute irure dolor in reprehenderit in voluptate velit esse cillum dolore eu fugiat nulla pariatur. Excepteur sint occaecat cupidatat non proident.</p>
  <div class="service-grid">
    <div class="service"><svg viewBox="0 0 52 52"><path d="M4 8h7l6 24h24l5-16H14"/><circle cx="20" cy="42" r="3"/><circle cx="38" cy="42" r="3"/></svg>Grocery shopping</div>
    <div class="service c2"><svg viewBox="0 0 52 52"><path d="M19 6h14v13h13v14H33v13H19V33H6V19h13z"/></svg>Medical<br>appointments</div>
    <div class="service c3"><svg viewBox="0 0 52 52"><path d="M14 30c-7-1-9-10-3-13 1-7 9-10 15-6 6-4 14-1 15 6 6 3 4 12-3 13v12H14z"/><path d="M14 36h24"/></svg>Meal preparation<br>&amp; cleanup</div>
    <div class="service r2"><svg viewBox="0 0 52 52"><path d="M40 6L26 26"/><path d="M22 22l10 8-8 14-16-10z"/><path d="M14 38l6-6M18 41l5-5"/></svg>Light<br>housekeeping</div>
    <div class="service c2 r2"><svg viewBox="0 0 52 52"><path d="M6 12v30M6 34h40v8M6 26h40v8"/><rect x="10" y="19" width="10" height="7"/></svg>Bed making</div>
    <div class="service c3 r2"><svg viewBox="0 0 52 52"><circle cx="22" cy="8" r="3"/><path d="M22 14v14h12l6 12"/><path d="M16 24a12 12 0 1 0 16 14"/></svg>Mobility<br>assistance</div>
    <div class="service r3"><svg viewBox="0 0 52 52"><path d="M4 14h28v22H4zM32 22h9l7 8v6H32"/><circle cx="12" cy="40" r="4"/><circle cx="40" cy="40" r="4"/></svg>Transportation</div>
    <div class="service c2 r3"><svg viewBox="0 0 52 52"><circle cx="18" cy="16" r="8"/><circle cx="34" cy="16" r="8"/><circle cx="18" cy="34" r="8"/><circle cx="34" cy="34" r="8"/></svg>Laundry</div>
    <div class="service c3 r3 more">Read More</div>
  </div>
</section>

<section class="why">
  <h2 class="abs heading red" style="left:54px;top:2050px;width:540px">Why non-medical in-home care &amp; companionship?</h2>
  <ul class="why-list">
    <li>Allows seniors to remain independent and in their own homes as long as possible.</li>
    <li>Provides a sense of comfort in familiar surroundings.</li>
    <li>Enhances quality of life.</li>
  </ul>
  <a class="btn-outline red" style="left:54px;top:2309px;width:188px;height:48px">Read More</a>
  <div class="abs why-photo" role="img" aria-label="Photo of two older women laughing together outdoors with a garden rake"></div>
</section>

<section class="finance">
  <div class="finance-photo" role="img" aria-label="Photo of a smiling older woman with short white hair and glasses"></div>
</section>
<h2 class="abs heading navy" style="left:54px;top:2622px">Financial effects of senior care</h2>
<div class="rule" style="left:54px;top:2680px;background:var(--red)"></div>
<p class="abs body-copy" style="left:54px;top:2700px;width:560px;font-size:14.5px;line-height:1.95">In the most recent Harborline Cost of Care Survey (2016), the following were the costs for the three most popular senior care options in Albany, New York:</p>
<table class="cost-table">
  <tr><th class="col1">Albany, NY</th><th class="col2">Average Costs</th><th>Annual Cost</th></tr>
  <tr><td>Assisted Living</td><td>$ 4,554/month</td><td>$ 54,648</td></tr>
  <tr><td>Nursing Home</td><td>$ 370/day</td><td>$ 135,050</td></tr>
  <tr><td>Senior home care</td><td>$ 24/hour</td><td>$ 37,440*</td></tr>
</table>
<a class="btn-outline" style="left:54px;top:2946px;width:188px;height:48px">Read More</a>

<section class="cards">
  <div class="card" style="left:54px"><div class="card-photo" role="img" aria-label="Photo of a caregiver handing a basket of laundry to an older woman"></div><h3 class="card-title">Who are junior-seniors?</h3></div>
  <div class="card" style="left:435px"><div class="card-photo" role="img" aria-label="Photo of a caregiver bringing a cup to a seated older woman"></div><h3 class="card-title">Do you need care?</h3></div>
  <div class="card" style="left:814px"><div class="card-photo" role="img" aria-label="Photo of a caregiver styling an older woman's hair"></div><h3 class="card-title">Does someone you love need care?</h3></div>
</section>

<footer class="site-footer">
  <div class="footer-brand"><span class="brand-square"></span><span class="brand-name">Maplebrook Elders</span></div>
  <h4 class="footer-heading" style="left:422px">Contact</h4>
  <ul class="contact-list">
    <li>P.O. Box 48, Alder Springs,</li>
    <li>New York 12099</li>
    <li>Phone:(555) 014-2290</li>
    <li>info@maplebrookelders.example</li>
  </ul>
  <div class="socials"><span></span><span></span><span></span><span></span><span></span><span></span></div>
  <h4 class="footer-heading" style="left:800px">Newsletter</h4>
  <p class="newsletter-text">Enter your email address to get the latest University news, special events and student activities delivered.</p>
  <div class="newsletter-form"><div class="field">Your Email-Id</div><div class="submit">Subscribe</div></div>
</footer>
<p class="legal">Maplebrook Elders © 2017 All Rights Reserved | Privacy Policy</p>

</body>
</html>
```